Letterhead and Stationary for Construction Company

Brisk Current needs modern Letterhead, Envelopes and Notepad designs.

Industry/Entity Type

Construction

Colors
f78f20
34a7d8
ffffff

Requirements
Must have
• Modern looking design.

```html
<!DOCTYPE html>
<html lang="en">
<head>
<meta charset="utf-8">
<title>Brisk Current Stationery</title>
<link rel="stylesheet" href="https://fonts.googleapis.com/css2?family=Montserrat:wght@500;700&display=swap">
<style>
:root{
  --stage:#c8c8c8;
  --paper:#ffffff;
  --orange:#f78f20;
  --orange-soft:#f9c08a;
  --blue:#2f86f5;
  --ink:#111111;
}
*{margin:0;padding:0;box-sizing:border-box}
html,body{width:1200px;height:1200px;overflow:hidden}
body{background:var(--stage);font-family:"Montserrat",Arial,sans-serif;position:relative}
.label{position:absolute;font-weight:700;font-size:26px;color:var(--ink);white-space:nowrap}
.label--letterhead{left:324px;top:142px;transform:translateX(-50%)}
.label--envelope{left:870px;top:142px;transform:translateX(-50%)}
.label--notepad{left:968px;top:704px}
.sheet{position:absolute;background:var(--paper)}
.letterhead{left:74px;top:193px;width:503px;height:706px}
.envelope{left:599px;top:198px;width:527px;height:268px}
.notepad{left:599px;top:504px;width:360px;height:503px}
.brand{position:absolute;display:flex;align-items:center;gap:6px;font-weight:700;color:var(--blue);white-space:nowrap;line-height:1}
.brand__dot{border-radius:50%;border:4px solid var(--orange);flex:none}
.letterhead .brand{left:49px;top:36px;font-size:21px}
.envelope .brand{left:36px;top:28px;font-size:19px}
.notepad .brand{left:117px;top:30px;font-size:20px}
.letterhead .brand__dot,.envelope .brand__dot,.notepad .brand__dot{width:34px;height:34px}
.rule-v{position:absolute;width:3px;background:var(--orange-soft)}
.rule-h{position:absolute;height:3px;background:var(--orange-soft)}
.icon{position:absolute;width:16px;height:16px;fill:var(--blue)}
.contact{position:absolute;font-size:5.5px;line-height:9px;color:var(--blue);font-weight:500;white-space:nowrap}
.contact--right{text-align:right}
.footer-line{position:absolute;left:10px;right:10px;height:2px;background:var(--orange-soft)}
.footer-band{position:absolute;left:0;right:0;bottom:0;background:var(--blue)}
</style>
</head>
<body>
<svg width="0" height="0" style="position:absolute">
  <defs>
    <symbol id="icon-pin" viewBox="0 0 16 16"><path d="M8 0a5.5 5.5 0 0 0-5.5 5.5C2.5 10 8 16 8 16s5.5-6 5.5-10.5A5.5 5.5 0 0 0 8 0zm0 8a2.5 2.5 0 1 1 0-5 2.5 2.5 0 0 1 0 5z"/></symbol>
    <symbol id="icon-phone" viewBox="0 0 16 16"><path d="M1 5c0-2 3-3 7-3s7 1 7 3v1.5h-3.5V5h-7v1.5H1z"/><path d="M3.5 7.5h9l1.5 7H2z"/><circle cx="8" cy="11" r="1.8" fill="#fff"/></symbol>
    <symbol id="icon-globe" viewBox="0 0 16 16"><circle cx="8" cy="8" r="7.5"/><path d="M4 4c2 0 3 1 2.5 2.5S5 9 6 11l-1 3M10 2c-1 2 1 3 2.5 3M11 9c1.5 0 2 2 1 4" stroke="#fff" stroke-width="1.1" fill="none"/></symbol>
  </defs>
</svg>

<div class="label label--letterhead">Letterhead</div>
<div class="label label--envelope">DL Envelope</div>
<div class="label label--notepad">A5 Notepad</div>

<section class="sheet letterhead" aria-label="Letterhead">
  <div class="brand"><span class="brand__dot"></span>Brisk Current</div>
  <div class="rule-v" style="left:107px;top:85px;height:426px"></div>
  <svg class="icon" style="left:101px;top:516px"><use href="#icon-pin"/></svg>
  <div class="contact contact--right" style="left:20px;width:96px;top:541px">123 Street Name, Town/City<br>State, County, Zip</div>
  <div class="rule-h" style="left:25px;width:86px;top:566px"></div>
  <svg class="icon" style="left:101px;top:575px"><use href="#icon-phone"/></svg>
  <div class="contact contact--right" style="left:20px;width:96px;top:597px">Tel: +00 999 456 789<br>Tel: +00 999 456 789</div>
  <div class="rule-h" style="left:25px;width:86px;top:620px"></div>
  <svg class="icon" style="left:101px;top:633px"><use href="#icon-globe"/></svg>
  <div class="contact contact--right" style="left:20px;width:96px;top:654px">info@yourcompany.com<br>www.yourcompany.com</div>
  <div class="footer-line" style="top:683px"></div>
  <div class="footer-band" style="height:18px"></div>
</section>

<section class="sheet envelope" aria-label="DL Envelope">
  <div class="brand"><span class="brand__dot"></span>Brisk Current</div>
  <div class="rule-v" style="left:97px;top:76px;height:120px"></div>
  <svg class="icon" style="left:91px;top:209px;width:14px;height:14px"><use href="#icon-globe"/></svg>
  <div class="contact contact--right" style="left:20px;width:85px;top:228px">info@yourcompany.com<br>www.yourcompany.com</div>
</section>

<section class="sheet notepad" aria-label="A5 Notepad">
  <div class="brand"><span class="brand__dot"></span>Brisk Current</div>
  <svg class="icon" style="left:90px;top:429px"><use href="#icon-pin"/></svg>
  <div class="contact contact--right" style="left:4px;width:100px;top:455px">123 Street Name, Town/City<br>State, County, Zip</div>
  <div class="rule-v" style="left:126px;top:427px;height:49px"></div>
  <svg class="icon" style="left:203px;top:430px"><use href="#icon-phone"/></svg>
  <div class="contact" style="left:147px;top:455px">Tel: +00 999 456 789<br>Tel: +00 999 456 789</div>
  <div class="rule-v" style="left:244px;top:427px;height:49px"></div>
  <svg class="icon" style="left:326px;top:430px"><use href="#icon-globe"/></svg>
  <div class="contact contact--right" style="left:250px;width:94px;top:455px">info@yourcompany.com<br>www.yourcompany.com</div>
  <div class="footer-line" style="top:481px"></div>
  <div class="footer-band" style="height:17px"></div>
</section>
</body>
</html>
```